Bright Summit Web Design

I am starting a new company that will provide LIFE COACHING services - I have tried to design a website, but it's too complicated. Right now, it's just me - I'm the only person that will provide services through the website - I have used makerhive to purchase a logo (see below). I want to be able to update the website myself, but need a template - basic design. Because I am not technologically savvy enough to explain in words - I basically want to have a website that will provide basic information about my services (coaching), a page about me and my background, hopefully scheduling possibilities, and testimonials — also a page for writing/blogs. I bought a website through NetBarn - so when I have a template, I guess I”d use that - but maybe I’ll need to work with a designer to actually get it up on the internet. I have a head shot that I’ll upload, too.
Clients from the independent (private school) world - teachers, administrators
4 page

```html
<!DOCTYPE html>
<html lang="en">
<head>
<meta charset="utf-8">
<title>Bright Summit Coaching</title>
<link rel="stylesheet" href="https://fonts.googleapis.com/css2?family=Nunito:wght@400;600;700;800&display=swap">
<style>
:root{
  --teal:#1aae97;
  --teal-dark:#12917d;
  --teal-pale:#e6f6f3;
  --ink:#2e3438;
  --muted:#6b7378;
  --line:#d9e2e0;
  --dark:#3a3b3d;
  --darker:#2c2d2f;
  --white:#ffffff;
}
*{box-sizing:border-box;margin:0;padding:0}
html,body{width:1200px;height:3784px;overflow:hidden}
body{font-family:'Nunito',sans-serif;color:var(--ink);background:var(--white);position:relative}
.abs{position:absolute}
.btn{display:inline-block;background:var(--teal);color:var(--white);font-weight:800;font-size:14px;letter-spacing:.5px;padding:12px 28px;border-radius:24px;text-transform:uppercase;white-space:nowrap}
.btn.white{background:var(--white);color:var(--teal)}
.label{color:var(--teal);font-size:11px;font-weight:700;letter-spacing:1px;text-transform:uppercase}
.ph{position:absolute}

/* header */
.header-band{top:0;left:0;width:1200px;height:110px;background:var(--white);z-index:4}
.hdr{z-index:5}
.topbar{top:22px;font-size:13px;color:var(--muted);white-space:nowrap}
.topbar b{color:var(--ink)}
.brand{top:24px;left:40px;display:flex;align-items:center;gap:10px}
.brand .dot{width:40px;height:40px;border-radius:50%;background:var(--teal)}
.brand span{font-size:22px;font-weight:800;color:var(--teal)}
.nav{top:68px;left:400px;display:flex;gap:26px;font-size:13px;font-weight:700;text-transform:uppercase;white-space:nowrap}
.nav .on{color:var(--teal);border-bottom:2px solid var(--teal);padding-bottom:4px}
.nav-cta{top:58px;left:910px;padding:10px 22px;font-size:12px}

/* hero */
.hero-photo{left:600px;top:110px;width:600px;height:550px;background:linear-gradient(135deg,#f2efe9,#d8c3ad 55%,#b98e70)}
.hero-ring{left:600px;top:110px}
.hero-title{left:40px;top:285px;font-size:54px;line-height:1.1;font-weight:700}
.hero-title .t{color:var(--teal)}
.hero-text{left:40px;top:420px;width:380px;font-size:16px;line-height:1.5;color:var(--muted)}
.hero-btn{left:40px;top:500px}

/* services */
.sec-head{width:1200px;text-align:center}
.sec-head h2{font-size:42px;font-weight:800;margin-top:6px}
.cards{left:40px;display:grid;grid-template-columns:repeat(3,353px);gap:30px}
.svc .img{height:180px}
.svc .bar{height:50px;background:var(--teal);color:var(--white);font-weight:800;font-size:20px;display:flex;align-items:center;justify-content:center}

/* about */
.about-bg{top:1380px;left:0;width:1200px;height:780px;background:linear-gradient(90deg,#fff,#f4f7f6)}
.about-photo{left:600px;top:1420px;width:560px;height:740px;background:linear-gradient(180deg,#ecefee,#b9a89a 60%,#2d2f33)}
.about-ring{left:60px;top:1500px}
.about-copy{left:160px;top:1610px;width:300px;text-align:center}
.about-copy h2{font-size:36px;line-height:1.15;font-weight:600;color:var(--ink)}
.about-copy h2 b{color:var(--teal);font-weight:800}
.about-copy p{font-size:13px;line-height:1.6;color:var(--muted);margin-top:16px}
.sign{width:160px;height:40px;margin:18px auto 0;background:linear-gradient(90deg,#cfd6d4,#9aa3a1);border-radius:4px}

/* testimonials */
.testi{top:2160px;left:0;width:1200px;height:460px;background:linear-gradient(90deg,#2b2a2b,#4a3e37 50%,#2b2c30)}
.testi-h{left:160px;top:2210px;color:var(--white)}
.testi-h h2{font-size:40px;font-weight:800}
.testi-all{left:860px;top:2235px;padding:9px 20px;font-size:12px}
.quote{width:280px;height:140px;background:var(--teal);color:var(--white);font-size:14px;line-height:1.55;padding:22px 24px;border-radius:4px}
.who{color:var(--white);font-weight:800;font-size:14px;margin-top:14px}
.stars{color:var(--teal);font-size:16px;letter-spacing:2px}
.arrow{font-size:13px;font-weight:700;color:var(--white);display:flex;align-items:center;gap:8px}
.arrow.dk{color:var(--ink)}

/* blogs */
.blog-h{left:160px;top:2660px}
.blog-h h2{font-size:40px;font-weight:800}
.blog-all{left:940px;top:2690px;padding:9px 22px;font-size:12px;background:var(--ink)}
.post{width:280px;box-shadow:0 4px 14px rgba(0,0,0,.1)}
.post .img{height:200px;position:relative}
.post .plus{position:absolute;left:0;top:0;width:44px;height:44px;background:var(--teal);color:#fff;font-size:28px;display:flex;align-items:center;justify-content:center}
.post .body{padding:18px 20px;height:200px;background:#fff}
.post h3{font-size:22px;line-height:1.2;font-weight:800}
.post p{font-size:13px;color:var(--muted);margin-top:10px;line-height:1.5}
.post .meta{font-size:12px;color:var(--muted);margin-top:12px;display:flex;gap:24px}

/* contact */
.contact{top:3220px;left:0;width:1200px;height:220px;background:var(--teal)}
.contact-h{left:160px;top:3270px;color:var(--white);font-size:40px;font-weight:600;letter-spacing:1px}
.contact-btn{left:160px;top:3340px}
.contact-info{left:780px;top:3265px;color:var(--white);font-size:16px;line-height:1.5}
.contact-info .big{font-size:28px;font-weight:800}
.contact-info .row{display:flex;gap:14px;align-items:flex-start;margin-bottom:14px}

/* footer */
.foot{top:3440px;left:0;width:1200px;height:344px;background:var(--dark)}
.fcol{top:3490px;color:#d7dbda;font-size:14px;line-height:1.8}
.fcol h4{color:var(--white);font-size:20px;font-weight:800;margin-bottom:8px}
.fbrand{left:800px;top:3490px;display:flex;align-items:center;gap:12px}
.fbrand .dot{width:48px;height:48px;border-radius:50%;background:var(--teal)}
.fbrand span{font-size:26px;font-weight:800;color:var(--white)}
.social{left:840px;top:3650px;display:flex;gap:14px}
.social i{width:34px;height:34px;border-radius:50%;background:var(--teal);display:block}
.copy{top:3734px;left:0;width:1200px;height:50px;background:var(--darker);color:#aeb3b2;font-size:12px;padding:18px 160px}
</style>
</head>
<body>

<!-- header -->
<div class="abs header-band"></div>
<div class="abs hdr brand"><div class="dot"></div><span>Bright Summit</span></div>
<div class="abs hdr topbar" style="left:690px">&#9742; Call us: <b>+1 555 010 2040</b></div>
<div class="abs hdr topbar" style="left:920px">&#9993; Email Us: info@brightsummit.com</div>
<nav class="abs hdr nav"><span class="on">Home</span><span>About</span><span>Services</span><span>Coaching</span><span>Blog</span><span>Contact</span></nav>
<a class="abs hdr btn nav-cta">Schedule an Appointment</a>

<!-- hero -->
<div class="ph hero-photo" role="img" aria-label="Smiling mother and daughters hugging"></div>
<svg class="abs hero-ring" width="600" height="550" viewBox="0 0 600 550"><circle cx="260" cy="280" r="235" fill="none" stroke="#1aae97" stroke-width="5"/></svg>
<h1 class="abs hero-title"><span class="t">Taking Care</span><br>of Your Life Issues!</h1>
<p class="abs hero-text">Get the motivation, guidance, and support you need to get your life on track. You don't need to struggle on your own anymore!</p>
<a class="abs btn hero-btn">Schedule an Appointment</a>

<!-- services -->
<div class="abs sec-head" style="top:760px"><div class="label">Our Coaching Offer</div><h2>Our Services</h2></div>
<div class="abs cards" style="top:840px">
  <div class="svc"><div class="img" role="img" aria-label="Person leaping on a cliff at dusk" style="background:linear-gradient(180deg,#d9d5cf,#8b8884)"></div><div class="bar">Confidence Coaching</div></div>
  <div class="svc"><div class="img" role="img" aria-label="Group sitting in a meeting room" style="background:linear-gradient(180deg,#e6e3df,#6b6560)"></div><div class="bar">Increasing Welfare</div></div>
  <div class="svc"><div class="img" role="img" aria-label="Colleagues shaking hands" style="background:linear-gradient(180deg,#c9a88a,#4f4a48)"></div><div class="bar">People and Relationships</div></div>
</div>
<div class="abs cards" style="top:1110px">
  <div class="svc"><div class="img" role="img" aria-label="Woman meditating at sunset" style="background:linear-gradient(180deg,#f2c36a,#b57a3a)"></div><div class="bar">Mental Care</div></div>
  <div class="svc"><div class="img" role="img" aria-label="Runner in a green field" style="background:linear-gradient(180deg,#d7e6ef,#7fa35a)"></div><div class="bar">Physical Care</div></div>
  <div class="svc"><div class="img" role="img" aria-label="Team celebrating at work" style="background:linear-gradient(180deg,#bfc9d3,#5d6a78)"></div><div class="bar">Personal Growth</div></div>
</div>

<!-- about -->
<div class="abs about-bg"></div>
<div class="ph about-photo" role="img" aria-label="Coach holding a coffee cup"></div>
<svg class="abs about-ring" width="500" height="520" viewBox="0 0 500 520"><circle cx="250" cy="260" r="240" fill="none" stroke="#1aae97" stroke-width="3"/></svg>
<div class="abs about-copy">
  <h2>Bright Summit<br><b>Transforms Lives</b></h2>
  <p>We help teachers and school leaders find clarity, balance and confidence through one to one coaching built around your goals and your pace.</p>
  <p>Each session offers calm, honest support so you can move forward with a plan that fits real life.</p>
  <div class="sign" role="img" aria-label="Handwritten signature"></div>
  <a class="btn" style="margin-top:22px">About Us</a>
</div>

<!-- testimonials -->
<div class="ph testi" role="img" aria-label="Friends laughing together in a cafe, darkened"></div>
<div class="abs testi-h"><div class="label">Testimonials</div><h2>Happy Client's</h2></div>
<a class="abs btn white testi-all">All Testimonials</a>
<div class="abs arrow" style="left:60px;top:2372px">&#8592; PREV</div>
<div class="abs arrow" style="left:1080px;top:2372px">NEXT &#8594;</div>
<div class="abs" style="left:160px;top:2320px"><div class="quote">Coaching gave me space to step back and plan. I left every session with clear steps and new energy for my classroom.</div><div class="who">SAM HOLLOWAY</div><div class="stars">&#9733;&#9733;&#9733;&#9733;&#9733;</div></div>
<div class="abs" style="left:460px;top:2320px"><div class="quote">I finally set limits that work. The support was kind, practical and focused on what I really wanted to change.</div><div class="who">SAM HOLLOWAY</div><div class="stars">&#9733;&#9733;&#9733;&#9733;&#9733;</div></div>
<div class="abs" style="left:780px;top:2320px"><div class="quote">A calm, thoughtful guide. My confidence as a new school leader grew week by week, and my team noticed too.</div><div class="who">SAM HOLLOWAY</div><div class="stars">&#9733;&#9733;&#9733;&#9733;&#9733;</div></div>

<!-- blogs -->
<div class="abs blog-h"><div class="label">Our Stories</div><h2>Latest blogs</h2></div>
<a class="abs btn blog-all">View All</a>
<div class="abs arrow dk" style="left:50px;top:2950px">&#8592; PREV</div>
<div class="abs arrow dk" style="left:1080px;top:2950px">NEXT &#8594;</div>
<div class="abs post" style="left:160px;top:2760px"><div class="img" role="img" aria-label="Person resting on a sofa" style="background:linear-gradient(180deg,#e8dfd2,#b79a78)"><div class="plus">+</div></div><div class="body"><h3>Thoughts on Procrastination</h3><p>Why we delay the things that matter and small ways to start today.</p><div class="meta"><span>&#9719; Jan 12, 2021</span><span>&#9675; 0 Comments</span></div></div></div>
<div class="abs post" style="left:460px;top:2760px"><div class="img" role="img" aria-label="Smiling cafe team in aprons" style="background:linear-gradient(180deg,#d8c8b4,#6e5a48)"><div class="plus">+</div></div><div class="body"><h3>People who made inspiring life changes</h3><p>Real stories of educators who chose a new path and grew.</p><div class="meta"><span>&#9719; Jan 12, 2021</span><span>&#9675; 0 Comments</span></div></div></div>
<div class="abs post" style="left:760px;top:2760px"><div class="img" role="img" aria-label="Green grass close-up with a figure" style="background:linear-gradient(180deg,#cfe0b8,#4f8a3a)"><div class="plus">+</div></div><div class="body"><h3>The incredible power of small changes</h3><p>Tiny daily habits that add up to lasting, meaningful progress.</p><div class="meta"><span>&#9719; Jan 12, 2021</span><span>&#9675; 0 Comments</span></div></div></div>

<!-- contact -->
<div class="abs contact"></div>
<svg class="abs" style="left:0;top:3220px" width="1200" height="220" viewBox="0 0 1200 220"><polygon points="700,0 1200,0 1200,220 640,220" fill="#12917d"/></svg>
<div class="abs contact-h">FEEL FREE TO CONTACT US</div>
<a class="abs btn white contact-btn">Schedule an Appointment</a>
<div class="abs contact-info">
  <div class="row"><svg width="24" height="24" viewBox="0 0 24 24"><path d="M6 2l4 4-2 3c1 2 3 4 5 5l3-2 4 4-3 4C10 20 4 14 2 5z" fill="#fff"/></svg><span class="big">+1 555 010 2040</span></div>
  <div class="row"><svg width="24" height="24" viewBox="0 0 24 24"><path d="M12 2a7 7 0 0 0-7 7c0 5 7 13 7 13s7-8 7-13a7 7 0 0 0-7-7zm0 9.5A2.5 2.5 0 1 1 12 6.5a2.5 2.5 0 0 1 0 5z" fill="#fff"/></svg><span>123, Your Address,<br>United States, N 10U</span></div>
  <div class="row"><svg width="24" height="24" viewBox="0 0 24 24"><rect x="2" y="5" width="20" height="14" rx="2" fill="#fff"/><path d="M2 6l10 7 10-7" stroke="#12917d" stroke-width="2" fill="none"/></svg><span>info@brightsummit.com</span></div>
</div>

<!-- footer -->
<div class="abs foot"></div>
<div class="abs fcol" style="left:160px"><h4>Office Hours</h4>Mon - Wed : 8am - 7pm<br>Thursday : 8am - 5pm<br>Friday : 8am - 4pm<br>Sat - Sun : Closed</div>
<div class="abs fcol" style="left:390px"><h4>Usefull Links</h4>About<br>Coaching<br>Blog<br>Privacy Policy<br>Terms &amp; Conditions</div>
<div class="abs fcol" style="left:560px"><h4>Services</h4>Consultancy &amp; Advising<br>Problem Solving<br>Conferencing &amp; Talks</div>
<div class="abs fbrand"><div class="dot"></div><span>Bright Summit</span></div>
<div class="abs social"><i></i><i></i><i></i></div>
<div class="abs copy">Copyright &copy; Bright Summit 2021. All Rights Reserved.</div>

</body>
</html>
```